Computer Training in the Education sector - Letterhead

We need a new letter head to be designed for the company. We provide computer training fro the Education Sector, both primary and private tertiary providers. The colours will need to tie in with the website www.crossingtheriver.co.nz.
The company name is Crossing the River with the tag line of Computer Training for Educators.
The footer will need to have the following detail...
0508 PCS TUTOR
021 847 193
www.crossingtheriver.co.nz / training@crossingtheriver.co.nz
Updates

Thanks for the designs so far.

Some have watermarks in the background. Please don't worry about using watermarks as I will not be using a watermark in in a final design.
Regards,
Warren

Thank you for all the designs and the effort. There was some great concepts that came through.

Cheers
Warren

Industry/Entity Type

Computer

```html
<!DOCTYPE html>
<html lang="en">
<head>
<meta charset="utf-8">
<title>Crossing the River – Letterhead</title>
<link rel="stylesheet" href="https://fonts.googleapis.com/css2?family=Tinos&display=swap">
<style>
  :root {
    --paper: #ffffff;
    --accent-green: #8fe52b;
    --accent-orange: #ef883b;
    --accent-blue: #2f80e8;
    --text-blue: #2468d0;
  }
  * { margin: 0; padding: 0; box-sizing: border-box; }
  html, body {
    width: 848px;
    height: 1200px;
    overflow: hidden;
    background: var(--paper);
  }
  .letterhead {
    position: relative;
    width: 848px;
    height: 1200px;
    background: var(--paper);
    font-family: "Tinos", "Times New Roman", serif;
    color: var(--text-blue);
  }
  .corner-shapes {
    position: absolute;
    inset: 0;
    width: 848px;
    height: 1200px;
  }
  .brand {
    position: absolute;
    top: 78px;
    right: 48px;
    width: 220px;
    text-align: center;
  }
  .brand-name {
    font-size: 30px;
    line-height: 1.05;
    font-weight: 400;
    color: var(--accent-blue);
  }
  .brand-web {
    position: absolute;
    top: 190px;
    right: 48px;
    font-size: 14px;
    letter-spacing: 1.2px;
  }
  .contact {
    position: absolute;
    left: 48px;
    top: 1090px;
    list-style: none;
    font-size: 15px;
    line-height: 24.5px;
    letter-spacing: 1.2px;
  }
</style>
</head>
<body>
  <main class="letterhead">
    <svg class="corner-shapes" viewBox="0 0 848 1200" aria-hidden="true">
      <polygon class="band-green" points="0,0 114,0 0,341" fill="var(--accent-green)"/>
      <polygon class="band-orange" points="114,0 138,0 0,414 0,341" fill="var(--accent-orange)"/>
      <polygon class="band-blue" points="848,742 848,1200 718,1200" fill="var(--accent-blue)"/>
    </svg>

    <header class="brand">
      <p class="brand-name">Crossing<br>the River</p>
    </header>
    <p class="brand-web">www.crossingtheriver.co.nz</p>

    <ul class="contact">
      <li>0508 PCS TUTOR</li>
      <li>021 847 193</li>
      <li>training@crossingtheriver.co.nz</li>
    </ul>
  </main>
</body>
</html>
```